Small Business Broker Business Card Design

A business card design for a small business brokerage, which is a financial service, not unlike real estate brokerage, but for small businesses such as laundromats, pizza shops, restaurants, cleaners etc. The designs should all be simple, more conservative in nature, using the colors and font of the logo. Again, think real estate Brokerage as a business context
Contact Information for Business Card
Name: Milo R. Dunbar. Title: Small Business Advisor. Email: m.dunbar@harborstoneadvisory.com. Mobile: (917) 555-0148. Office: (718) 555-0193. www.harborstoneadvisory.com

```html
<!DOCTYPE html>
<html lang="en">
<head>
<meta charset="utf-8">
<title>Harborstone Advisory – Business Card</title>
<link rel="stylesheet" href="https://fonts.googleapis.com/css2?family=Open+Sans:wght@400;600;700&display=swap">
<style>
  :root {
    --navy: #1b3a6b;
    --navy-deep: #14305c;
    --green: #8cc63f;
    --ink: #1d1d1d;
    --paper: #ffffff;
    --stage: #232323;
  }
  html, body {
    margin: 0;
    padding: 0;
    width: 1200px;
    height: 780px;
    overflow: hidden;
    background: var(--stage);
    font-family: "Open Sans", Arial, sans-serif;
  }
  .canvas {
    position: relative;
    width: 1200px;
    height: 780px;
  }
  .card {
    position: absolute;
    top: 241px;
    width: 520px;
    height: 298px;
    overflow: hidden;
  }
  .card--front { left: 50px; background: var(--paper); }
  .card--back { left: 630px; background: var(--navy); }

  .front-swoosh {
    position: absolute;
    inset: 0;
    width: 100%;
    height: 100%;
  }
  .brand {
    position: absolute;
    left: 34px;
    top: 48px;
    display: flex;
    align-items: center;
    gap: 10px;
  }
  .brand__mark {
    width: 22px;
    height: 22px;
    background: var(--navy);
    flex: none;
  }
  .brand__name {
    font-weight: 700;
    font-size: 15px;
    line-height: 1.15;
    color: var(--navy);
    text-transform: uppercase;
    letter-spacing: 0.5px;
  }
  .divider {
    position: absolute;
    left: 228px;
    top: 34px;
    width: 1.5px;
    height: 150px;
    background: var(--ink);
  }
  .contact {
    position: absolute;
    left: 246px;
    top: 30px;
    color: var(--ink);
  }
  .contact__name {
    margin: 0;
    font-size: 25px;
    font-weight: 700;
    line-height: 1.1;
  }
  .contact__first { color: var(--green); }
  .contact__last { color: var(--navy); }
  .contact__title {
    margin: 2px 0 8px;
    font-size: 13.5px;
  }
  .contact__address {
    margin: 0 0 6px;
    font-size: 13px;
    line-height: 1.3;
    font-style: normal;
  }
  .contact__list {
    list-style: none;
    margin: 0;
    padding: 0;
    font-size: 12.5px;
    line-height: 1.45;
  }
  .contact__list li {
    display: flex;
    align-items: center;
    gap: 6px;
  }
  .contact__icon {
    width: 12px;
    height: 12px;
    flex: none;
  }

  .back-brand {
    position: absolute;
    inset: 0;
    display: flex;
    align-items: center;
    justify-content: center;
    gap: 14px;
  }
  .back-brand__mark {
    width: 30px;
    height: 30px;
    background: var(--navy-deep);
  }
  .back-brand__name {
    font-weight: 700;
    font-size: 22px;
    letter-spacing: 0.6px;
    text-transform: uppercase;
    color: var(--navy-deep);
  }
</style>
</head>
<body>
<main class="canvas">

  <section class="card card--front" aria-label="Business card front">
    <svg class="front-swoosh" viewBox="0 0 520 298" preserveAspectRatio="none" aria-hidden="true">
      <path d="M0 150 C60 230 250 285 520 298 L0 298 Z" fill="var(--green)"/>
      <path d="M150 205 C260 260 400 285 520 297 C400 280 270 255 150 205 Z" fill="var(--paper)"/>
      <path d="M150 200 C270 258 400 282 520 296 L520 298 C395 286 265 262 150 200 Z" fill="var(--navy)"/>
    </svg>

    <div class="brand">
      <span class="brand__mark"></span>
      <span class="brand__name">Harborstone<br>Advisory, Inc</span>
    </div>

    <div class="divider"></div>

    <div class="contact">
      <h1 class="contact__name"><span class="contact__first">Milo R.</span> <span class="contact__last">Dunbar</span></h1>
      <p class="contact__title">Small Business Advisor</p>
      <address class="contact__address">480 Alder Row, Suite 310<br>Brookfield, NY 11201</address>
      <ul class="contact__list">
        <li>
          <svg class="contact__icon" viewBox="0 0 12 12" aria-hidden="true"><circle cx="6" cy="6" r="6" fill="var(--green)"/><path d="M4 3.2l1 1.4-.6.7c.4.9 1.1 1.6 2 2l.7-.6 1.4 1-.5 1C5.8 8.6 3.4 6.2 3.3 4.1z" fill="#fff"/></svg>
          (917) 555-0148
        </li>
        <li>
          <svg class="contact__icon" viewBox="0 0 12 12" aria-hidden="true"><circle cx="6" cy="6" r="6" fill="var(--green)"/><path d="M4 3.2l1 1.4-.6.7c.4.9 1.1 1.6 2 2l.7-.6 1.4 1-.5 1C5.8 8.6 3.4 6.2 3.3 4.1z" fill="#fff"/></svg>
          (718) 555-0193
        </li>
        <li>
          <svg class="contact__icon" viewBox="0 0 12 12" aria-hidden="true"><circle cx="6" cy="6" r="6" fill="var(--green)"/><rect x="3" y="4" width="6" height="4.2" fill="#fff"/><path d="M3 4l3 2.3L9 4" fill="none" stroke="var(--green)" stroke-width=".7"/></svg>
          m.dunbar@harborstoneadvisory.com
        </li>
        <li>
          <svg class="contact__icon" viewBox="0 0 12 12" aria-hidden="true"><circle cx="6" cy="6" r="6" fill="var(--green)"/><circle cx="6" cy="6" r="3.2" fill="none" stroke="#fff" stroke-width=".8"/><path d="M2.8 6h6.4M6 2.8c-1.5 1.8-1.5 4.6 0 6.4M6 2.8c1.5 1.8 1.5 4.6 0 6.4" fill="none" stroke="#fff" stroke-width=".7"/></svg>
          www.harborstoneadvisory.com
        </li>
      </ul>
    </div>
  </section>

  <section class="card card--back" aria-label="Business card back">
    <div class="back-brand">
      <span class="back-brand__mark"></span>
      <span class="back-brand__name">Harborstone Advisory, Inc</span>
    </div>
  </section>

</main>
</body>
</html>
```